New Zealand Export company needs business cards

We need new business cards to match our new logo for a company based in New Zealand who deal specifically with the Pacific Islands. We source, consolidate and ship products out of New Zealand to the Pacific Islands. Will attach our old ones and also new logo.
Would like the Islands we deal with and the areas of work we have access to, to be included on the business cards.

Contact Information for Business Card

T +64 9 571 3048
F +64 9 571 6285
12-18 Kowhai Lane, Drury, 2113
PO Box 814, Drury, Auckland 2247, New Zealand
www.falconfreight.example.nz
E sales@falconfreight.example.nz

Font styles to use
Sans Serif

Colors
85abd2
33a6d7
ffffff

Requirements
Must have
• A company of PWM

```html
<!DOCTYPE html>
<html lang="en">
<head>
<meta charset="utf-8">
<title>Falcon Freight business cards</title>
<link href="https://fonts.googleapis.com/css2?family=Poppins:wght@400;500;600&display=swap" rel="stylesheet">
<style>
  :root {
    --bg: #8d8d8f;
    --card: #1f1f20;
    --blue-deep: #0e5cb4;
    --blue-mid: #1d6fd0;
    --blue-light: #38b2e6;
    --text-grey: #5c5c5e;
    --rule: #16458a;
  }
  * { margin: 0; padding: 0; box-sizing: border-box; }
  html, body { width: 1200px; height: 960px; overflow: hidden; }
  body {
    background: var(--bg);
    font-family: "Poppins", sans-serif;
    display: flex; flex-direction: column; align-items: center; justify-content: center;
    gap: 36px;
  }
  .card {
    position: relative;
    width: 760px; height: 434px;
    background: var(--card);
    box-shadow: 0 10px 24px rgba(0,0,0,.25);
    overflow: hidden;
  }
  /* front */
  .brand-front {
    position: absolute; inset: 0;
    display: flex; align-items: center; justify-content: center; gap: 16px;
  }
  .brand-mark { width: 44px; height: 44px; background: var(--blue-mid); }
  .brand-name {
    color: var(--blue-mid); font-weight: 600; font-size: 40px; letter-spacing: 3px;
  }
  /* back */
  .band { position: absolute; left: 278px; top: 0; width: 70px; height: 434px; }
  .brand-vertical {
    position: absolute; left: 250px; top: 40px;
    transform-origin: 0 0; transform: rotate(90deg);
    color: var(--blue-mid); font-weight: 600; white-space: nowrap;
  }
  .brand-vertical .line1 { display: block; font-size: 64px; line-height: 1; letter-spacing: 2px; }
  .brand-vertical .line2 { display: block; font-size: 30px; line-height: 1.2; letter-spacing: 17px; }
  .details { position: absolute; left: 400px; top: 52px; width: 320px; }
  .person-name { color: var(--blue-mid); font-weight: 500; font-size: 20px; letter-spacing: .5px; }
  .person-role { color: var(--blue-light); font-size: 14px; margin-bottom: 10px; }
  .block { border-top: 1px solid var(--rule); padding: 14px 0 16px; color: var(--text-grey); font-size: 13.5px; line-height: 1.45; }
</style>
</head>
<body>
  <section class="card card-front">
    <div class="brand-front">
      <span class="brand-mark"></span>
      <span class="brand-name">FALCON FREIGHT</span>
    </div>
  </section>

  <section class="card card-back">
    <div class="brand-vertical">
      <span class="line1">FALCON</span>
      <span class="line2">FREIGHT</span>
    </div>
    <svg class="band" viewBox="0 0 70 434" aria-hidden="true">
      <rect width="70" height="434" fill="var(--blue-deep)"/>
      <polygon points="28,118 70,96 70,318 28,340" fill="var(--blue-light)"/>
    </svg>
    <div class="details">
      <div class="person-name">TESSA HARLOW</div>
      <div class="person-role">Sales Manager</div>
      <div class="block">12-18 Kowhai Lane, Drury, 2113<br>PO Box 814, Drury,<br>Auckland 2247, New Zealand</div>
      <div class="block">P : +64 9 571 3048<br>F : +64 9 571 6285</div>
      <div class="block">sales@falconfreight.example.nz<br>www.falconfreight.example.nz</div>
    </div>
  </section>
</body>
</html>
```